New Website Design for PALVO.org

We are looking for a new website design for PALVO.org. PALVO is a non profit home inspector association based in California. Home Inspectors are people that come out and look at a house before it's purchased to let the buyer know of any defects that may exist.
Our site is based on Joomla so if you'll be able to make a Joomla 3 template as well, please let us know (not required, but a bonus).
We would like to see designs that incorporate royal blue, white and chrome into the site as that's our main business colors.
We would like a place for rotating banners though they don't need to be the same size as the current site.
We would like navigation to be easier to manage with menus only across the top (via drop down menus) where we are going to sort out the items currently on the side. Possibly the front page could have a graphic link to separate portals for Realtors, Home Buyers and Inspectors, but that's just one option.
We would like a good mobile design or something that will scale easily to mobile.
The Find an Inspector feature is important and should stand out. The ZIM PALVOr site
Current home page feels a bit busy. Would like to simplify a bit.

```html
<!DOCTYPE html>
<html lang="en">
<head>
<meta charset="utf-8">
<title>PALVO – Home</title>
<link href="https://fonts.googleapis.com/css2?family=Open+Sans:ital,wght@0,400;0,600;1,400&family=Ubuntu:wght@500;700&display=swap" rel="stylesheet">
<style>
:root{
  --royal:#1e3a9a;
  --royal-dark:#0f2780;
  --ink:#111;
  --text:#555;
  --muted:#888;
  --line:#ddd;
  --panel:#f7f7f7;
  --card:#f0f0f0;
  --footer:#262626;
  --white:#fff;
}
*{margin:0;padding:0;box-sizing:border-box}
html,body{width:1029px;height:1200px;overflow:hidden;background:var(--white)}
body{font-family:'Open Sans',sans-serif;color:var(--text);position:relative}
.abs{position:absolute}

/* header */
.site-header{position:absolute;left:0;top:0;width:1029px;height:127px;border-bottom:1px solid var(--line)}
.brand{position:absolute;left:95px;top:12px;width:104px;height:104px;border-radius:50%;border:3px solid #9aa6c4;background:#eef1f8;display:flex;align-items:center;justify-content:center;font-weight:600;font-size:17px;color:var(--royal)}
.main-nav{position:absolute;top:44px;left:353px;display:flex;font-size:13.5px;color:#444}
.main-nav a{display:block;height:34px;line-height:34px;padding:0 18px 0 0;color:#444;text-decoration:none;margin-right:12px}
.main-nav a.active{background:#000;color:#fff;padding:0 19px;margin-right:10px}
.nav-pointer{position:absolute;left:379px;top:119px}

/* hero */
.hero{position:absolute;left:0;top:138px;width:1029px;height:309px;background:linear-gradient(90deg,#8a6a55 0%,#b89a84 35%,#d8d2cc 60%,#c8b8a8 80%,#a07e68 100%);border-bottom:2px solid #222}
.search-panel{position:absolute;left:95px;top:43px;width:241px;height:226px;background:rgba(40,64,150,.88);border-radius:3px;padding:14px 16px}
.search-panel h2{font-family:'Ubuntu',sans-serif;font-weight:500;font-size:17px;color:#fff;margin-bottom:10px;letter-spacing:.2px}
.field{background:#fff;border:1px solid #ccc;height:23px;margin-bottom:9px;font-size:8.5px;font-style:italic;color:#555;padding:6px 10px}
.field.tall{height:55px}
.btn-submit{position:absolute;right:15px;bottom:13px;background:#111;color:#fff;font-size:13px;padding:4px 16px;border-radius:2px;border:1px solid #555}
.dots{position:absolute;left:492px;top:289px;display:flex;gap:8px}
.dots i{width:9px;height:9px;border-radius:50%;background:#fff;display:block}
.dots i.on{background:#1a2fc0}

/* welcome */
.welcome-title{position:absolute;top:464px;width:1029px;text-align:center;font-size:31px;color:var(--ink);letter-spacing:.3px}
.welcome-title span{color:var(--royal)}
.welcome-text{position:absolute;left:97px;top:513px;width:840px;text-align:center;font-size:9.6px;line-height:17px}
.slider-arrows{position:absolute;left:496px;top:552px;display:flex;gap:4px}
.slider-arrows i{width:17px;height:17px;border-radius:50%;background:#ddd;display:block}
.dash{position:absolute;left:94px;width:843px;border-top:1px dashed #ccc}

/* feature cards */
.card{position:absolute;top:615px;width:269px;height:76px;background:var(--card)}
.card .num{position:absolute;left:13px;top:15px;width:47px;height:47px;border-radius:50%;background:#d4d4d4;color:#fff;font-size:14px;text-align:center;line-height:47px}
.card h3{position:absolute;left:83px;top:16px;font-weight:400;font-size:11.5px;color:var(--royal)}
.card p{position:absolute;left:83px;top:36px;width:150px;font-size:8.5px;line-height:12px;color:#333}
.card .go{position:absolute;right:0;top:0;width:31px;height:76px;background:#e2e2e2}

/* about */
.about-title{position:absolute;left:94px;top:732px;font-size:31px;color:var(--ink)}
.about-text{position:absolute;left:94px;top:776px;width:556px;font-size:9.8px;line-height:17.2px}
.trial{position:absolute;left:685px;top:741px;width:247px;height:142px;background:linear-gradient(180deg,#1f45c0,#0c2a8a);border:1px solid #0a1f66;color:#fff;text-align:center;padding-top:12px}
.trial h2{font-family:'Ubuntu',sans-serif;font-weight:500;font-size:20px}
.trial p{font-size:9.5px;line-height:17px;text-align:justify;padding:4px 11px 0}
.btn-download{position:absolute;left:34px;top:97px;width:178px;height:31px;background:linear-gradient(#fff,#ddd);border-radius:3px;color:#333;font-family:'Ubuntu',sans-serif;font-weight:500;font-size:14px;display:flex;align-items:center;justify-content:center;gap:14px}

/* info band */
.info{position:absolute;left:0;top:910px;width:1029px;height:241px;background:var(--panel)}
.col{position:absolute;top:18px}
.col h3{font-family:'Ubuntu',sans-serif;font-weight:500;font-size:15px;color:#555;margin-bottom:12px}
.links li{list-style:none;font-size:11px;color:#444;margin-bottom:16px}
.links a{color:var(--royal-dark)}
.event{font-size:9.5px;line-height:15.5px;text-align:justify;width:211px;padding-bottom:8px;margin-bottom:8px;border-bottom:1px solid #e6e6e6;color:#666}
.event a{color:var(--royal-dark);font-weight:600}
.event:last-child{border:0}
.vline{position:absolute;top:20px;height:203px;border-left:1px solid #e0e0e0}
.login label{display:block;font-size:10.5px;color:#555;margin:14px 0 6px}
.login .input{width:208px;height:22px;background:#fff;border:1px solid #ccc}
.btn-login{display:inline-block;margin-top:13px;background:var(--royal-dark);color:#fff;font-size:10px;padding:7px 15px}
.forgot{position:absolute;left:144px;top:200px;font-size:9.5px;color:var(--royal-dark);text-decoration:underline;font-weight:600}

/* footer */
.site-footer{position:absolute;left:0;top:1151px;width:1029px;height:49px;background:var(--footer);font-size:10.5px;color:#888}
.site-footer nav{position:absolute;left:94px;top:18px;display:flex;gap:24px}
.site-footer .copy{position:absolute;right:94px;top:18px;font-size:9.5px}
</style>
</head>
<body>

<header class="site-header">
  <div class="brand">PALVO</div>
  <nav class="main-nav">
    <a class="active">Home</a><a>Find an Inspector</a><a>Home Buyers &amp; Seller</a><a>Real Estate Agents</a><a>Inspectors</a>
  </nav>
  <svg class="nav-pointer" width="14" height="8"><path d="M0 8 L7 0 L14 8Z" fill="#000"/></svg>
</header>

<section class="hero" role="img" aria-label="Banner photo: smiling home inspector with a clipboard in front of a brick house">
  <form class="search-panel">
    <h2>SEARCH FOR INSPECTOR</h2>
    <div class="field">Enter your name...</div>
    <div class="field">Distance..</div>
    <div class="field tall">Enter a zip or country</div>
    <div class="btn-submit">Submit</div>
  </form>
  <div class="dots"><i></i><i class="on"></i><i></i></div>
</section>

<h1 class="welcome-title" style="font-weight:400">WELCOME TO <span>CALIFORNIA REAL ESTATE</span></h1>
<p class="welcome-text">Lorem ipsum dolor sit amet, consectetuer adipiscing elit, sed diam nonummy nibh euismod tincidunt ut laoreet dolore magna aliquam erat volutpat. Ut wisi enim ad minim veniam, quis nostrud exerci tation ullamcorper suscipit lobortis nisl ut aliquip ex ea commodo consequat. Duis autem vel eum iriure dolor in hendrerit in vulputate velit esse molestie consequat .</p>
<div class="slider-arrows"><i></i><i></i></div>

<div class="dash" style="top:601px"></div>

<div class="card" style="left:94px"><span class="num">01.</span><h3>Path to Success</h3><p>Lorem Ipsum Dolor Sit amet and setting industry</p><span class="go"></span></div>
<div class="card" style="left:381px"><span class="num">02.</span><h3>Educational Publications</h3><p>Lorem Ipsum Dolor Sit amet and setting industry</p><span class="go"></span></div>
<div class="card" style="left:668px"><span class="num">03.</span><h3>Ask Palvo</h3><p>Lorem Ipsum Dolor Sit amet and setting industry</p><span class="go"></span></div>

<div class="dash" style="top:707px"></div>

<h2 class="about-title" style="font-weight:400">About Us</h2>
<p class="about-text">Lorem ipsum dolor sit amet, consectetuer adipiscing elit, sed diam nonummy nibh euismod tincidunt ut laoreet dolore magna aliquam erat volutpat. Ut wisi enim ad minim veniam, quis nostrud exerci tation ullamcorper suscipit lobortis nisl ut aliquip ex ea commodo consequat. Duis autem vel eum iriure dolor in hendrerit in vulputate velit esse molestie consequat .Lorem ipsum dolor sit amet, consectetuer adipiscing elit, sed diam nonummy nibh euismod tincidunt ut laoreet dolore magna aliquam erat volutpat. Ut wisi enim ad minim veniam, quis nostrud exerci tation ullamcorper suscipit lobortis nisl ut aliquip ex ea commodo consequat. Duis autem vel eum iriure dolor in hendrerit .</p>

<aside class="trial">
  <h2>Download Free Trial</h2>
  <p>Lorem ipsum dolor sit amet, consectetuer adipiscing elit, sed diam nonummy nibh euismod tincidunt ut laoreet dolore magna aliquam.</p>
  <div class="btn-download">
    <svg width="18" height="18" viewBox="0 0 18 18"><path d="M6 1h6v7h4l-7 7-7-7h4z" fill="#333"/><rect x="1" y="16" width="16" height="2" fill="#333"/></svg>
    Download Now
  </div>
</aside>

<section class="info">
  <div class="col" style="left:99px">
    <h3>Home Inspection Software</h3>
    <ul class="links">
      <li>California Real Estate Inspection Law</li>
      <li>PALVO Chapter Meeting Locations</li>
      <li>Standards of Practice</li>
      <li>Code of Ethics</li>
      <li>Education / CEC's</li>
      <li style="font-size:12px"><a>View More</a></li>
    </ul>
  </div>
  <div class="vline" style="left:375px"></div>
  <div class="col" style="left:392px">
    <h3>Upcoming Events</h3>
    <p class="event">Lorem ipsum dolor sit amet, consectetuer adipiscing elit, sed diam nonummy nibh euismod tincidunt ut. <a><u>09-08-2013</u></a></p>
    <p class="event">Lorem ipsum dolor sit amet, consectetuer adipiscing elit, sed diam nonummy nibh euismod tincidunt. <a><u>09-08-2013</u></a></p>
    <p class="event">Lorem ipsum dolor sit amet, consectetuer adipiscing elit, sed diam nonummy nibh euismod tincidunt. <a><u>09-08-2013</u></a></p>
  </div>
  <div class="vline" style="left:655px"></div>
  <div class="col login" style="left:701px;width:220px">
    <h3 style="margin-bottom:6px">Inspector Login</h3>
    <p style="font-size:9.5px">Lorem ipsum dolor sit amet, consectetuer</p>
    <label>Username</label><div class="input"></div>
    <label style="margin-top:9px">Password</label><div class="input"></div>
    <span class="btn-login">LOGIN</span>
    <span class="forgot">Forgot Login?</span>
  </div>
</section>

<footer class="site-footer">
  <nav><span>Home</span><span>Find an Inspector</span><span>Home Buyers &amp; Seller</span><span>Real Estate Agents</span><span>Inspectors</span></nav>
  <span class="copy">All Rights Reserved | Copyright 2012.</span>
</footer>

</body>
</html>
```